kestrel home systems HERS

Looking for business card design that represents our company. we are kestrel home systems and we dedicate our skills of home energy efficiency to our customer by providing energy solution to their energy problems.
HVAC
SOLAR
INSULLATION
LIGHTING
DUCT TESTING
HERS RATING.

```html
<!DOCTYPE html>
<html lang="en">
<head>
<meta charset="utf-8">
<title>Kestrel Home Systems – Business Card</title>
<link rel="stylesheet" href="https://fonts.googleapis.com/css2?family=Roboto:wght@400;500;700&family=Roboto+Condensed:wght@700&display=swap">
<style>
  :root {
    --page-bg: #e6e4e1;
    --card-white: #f3f3f3;
    --sky-blue: #00aeef;
    --leaf-green: #8dc63f;
    --ink-black: #000000;
    --ink-dark: #1d1d1d;
    --text-white: #ffffff;
  }
  * { margin: 0; padding: 0; box-sizing: border-box; }
  html, body { width: 1200px; height: 960px; overflow: hidden; }
  body {
    position: relative;
    background: var(--page-bg);
    font-family: "Roboto", Arial, sans-serif;
  }
  .card {
    position: absolute;
    width: 598px;
    height: 342px;
    border-radius: 18px;
    overflow: hidden;
  }
  .card-front { left: 315px; top: 113px; background: var(--card-white); }
  .card-back  { left: 312px; top: 472px; height: 340px; background: var(--ink-black); }

  .front-wave { position: absolute; inset: 0; width: 100%; height: 100%; }

  .brand-lockup {
    position: absolute;
    left: 46px;
    top: 56px;
    display: flex;
    align-items: center;
    gap: 10px;
  }
  .brand-dot {
    width: 26px; height: 26px;
    border-radius: 50%;
    background: var(--sky-blue);
  }
  .brand-name {
    font-weight: 700;
    font-size: 24px;
    color: var(--ink-dark);
    text-transform: uppercase;
    letter-spacing: 0.5px;
  }

  .contact-block {
    position: absolute;
    right: 37px;
    top: 114px;
    text-align: right;
    color: var(--text-white);
  }
  .person-name {
    font-family: "Roboto Condensed", "Arial Narrow", sans-serif;
    font-weight: 700;
    font-size: 23px;
    line-height: 1.1;
    letter-spacing: 0.3px;
  }
  .person-title { font-size: 14.5px; font-weight: 500; line-height: 1.2; }
  .address { margin-top: 12px; font-size: 14.5px; line-height: 18px; }
  .contact-list { margin-top: 9px; list-style: none; font-size: 14.5px; }
  .contact-list li {
    display: flex;
    justify-content: flex-end;
    align-items: center;
    gap: 4px;
    height: 19px;
  }
  .contact-list svg { width: 14px; height: 14px; fill: var(--text-white); flex: none; }

  .back-mark {
    position: absolute;
    left: 0; right: 0;
    top: 98px;
    display: flex;
    align-items: center;
    justify-content: center;
    gap: 14px;
  }
  .back-dot {
    width: 92px; height: 92px;
    border-radius: 50%;
    background: var(--sky-blue);
  }
  .back-name {
    font-weight: 700;
    font-size: 22px;
    color: var(--text-white);
    text-transform: uppercase;
    letter-spacing: 0.5px;
  }
  .service-list {
    position: absolute;
    left: 0; right: 0;
    top: 290px;
    text-align: center;
    color: var(--text-white);
    font-size: 14.5px;
  }
  .service-sep {
    display: inline-block;
    width: 5px; height: 5px;
    border-radius: 50%;
    background: var(--sky-blue);
    margin: 0 3px;
    vertical-align: middle;
  }
</style>
</head>
<body>

<section class="card card-front">
  <svg class="front-wave" viewBox="0 0 598 342" preserveAspectRatio="none" aria-hidden="true">
    <path fill="var(--leaf-green)" d="M0 244 C 90 284, 200 300, 290 205 S 460 0, 560 0 L598 0 L598 342 L0 342 Z"/>
    <path fill="var(--sky-blue)" stroke="#ffffff" stroke-width="2.5" d="M0 250 C 90 298, 215 316, 315 214 S 500 6, 600 -2 L600 344 L-2 344 Z"/>
  </svg>

  <div class="brand-lockup">
    <span class="brand-dot"></span>
    <span class="brand-name">Kestrel Home Systems</span>
  </div>

  <div class="contact-block">
    <h1 class="person-name">DANIEL REYES</h1>
    <p class="person-title">CEO/FOUNDER</p>
    <p class="address">1420 Alder Ridge Road<br>Fairbanks, Alaska 99712</p>
    <ul class="contact-list">
      <li>907 555 0148
        <svg viewBox="0 0 16 16"><path d="M3.6 1.5l2.3 2.6-1.2 1.8c.8 1.9 2.5 3.6 4.4 4.4l1.8-1.2 2.6 2.3-1.4 2.4C7 13.6 2.4 9 1.2 3z"/></svg></li>
      <li>907 555 0172
        <svg viewBox="0 0 16 16"><path d="M4.5 1h7v14h-7zM5.8 2.5v9.5h4.4V2.5zM8 12.8a.8.8 0 1 0 0 1.6.8.8 0 0 0 0-1.6z" fill-rule="evenodd"/></svg></li>
      <li>907 555 0193
        <svg viewBox="0 0 16 16"><path d="M4 1h7v4H4zM1 6h14v6h-2v3H3v-3H1zM4.5 10v3.5h7V10z" fill-rule="evenodd"/></svg></li>
      <li>daniel@kestrelhomesys.com
        <svg viewBox="0 0 16 16"><path d="M1 3.5h14v9H1zM2 4.5l6 4.5 6-4.5z" fill-rule="evenodd"/></svg></li>
      <li>www.kestrelhomesys.com
        <svg viewBox="0 0 16 16"><path d="M8 1a7 7 0 1 0 0 14A7 7 0 0 0 8 1zM3.5 5.5l2.5-.5 1.5 2-1 2-2 .5zM9 3l2.5 1 .5 2.5-2 1.5-1.5-1zM9.5 10l2.5-.5-1 3-2 .5z" fill-rule="evenodd"/></svg></li>
    </ul>
  </div>
</section>

<section class="card card-back">
  <div class="back-mark">
    <span class="back-dot"></span>
    <span class="back-name">Kestrel Home Systems</span>
  </div>
  <p class="service-list">
    Hvac<span class="service-sep"></span>Solar<span class="service-sep"></span>Insullation<span class="service-sep"></span>Lighting<span class="service-sep"></span>Duct Testing<span class="service-sep"></span>Hers Rating.
  </p>
</section>

</body>
</html>
```